Granite, Zinc and Clay Roofing LLC needs a new business card

I need a new business card because I have a new address.
I do slate copper and tile roofs. My webpage is: www.granitezincandclayroofing.example

```html
<!DOCTYPE html>
<html lang="en">
<head>
<meta charset="utf-8">
<title>Granite, Zinc and Clay Roofing LLC – Business Card</title>
<link href="https://fonts.googleapis.com/css2?family=Bebas+Neue&family=Montserrat:wght@400;500&family=Old+Standard+TT&display=swap" rel="stylesheet">
<style>
  :root {
    --page: #ffffff;
    --front-blue: #6d9dc8;
    --ink: #111111;
    --back-grey: #444243;
    --tone-light: #7a7a7a;
    --white: #ffffff;
    --gold: #b59b55;
    --gold-dark: #8c7336;
  }
  * { margin: 0; padding: 0; box-sizing: border-box; }
  html, body {
    width: 706px; height: 1200px; overflow: hidden;
    background: var(--page);
  }
  .canvas { position: relative; width: 706px; height: 1200px; }

  /* Front side */
  .card-front {
    position: absolute; left: 21px; top: 0;
    width: 631px; height: 410px;
    background: var(--front-blue);
    color: var(--ink);
    overflow: hidden;
    font-family: "Old Standard TT", serif;
  }
  .front-person {
    position: absolute; right: 35px; top: 108px;
    text-align: right;
  }
  .front-name { font-size: 26px; letter-spacing: 0.5px; line-height: 1; }
  .front-name .paren { font-size: 40px; vertical-align: -6px; }
  .front-title { font-size: 18px; margin-top: 4px; }
  .front-mark {
    position: absolute; left: 140px; top: 290px;
    width: 26px; height: 26px;
    background: var(--ink);
  }
  .front-company {
    position: absolute; left: 185px; top: 280px;
    font-size: 34px;
    line-height: 1.2;
    color: var(--ink);
  }

  /* Back side */
  .card-back {
    position: absolute; left: 21px; top: 442px;
    width: 626px; height: 412px;
    background: var(--back-grey);
    overflow: hidden;
    box-shadow: 12px 14px 16px rgba(0,0,0,0.45);
  }
  .back-texture {
    position: absolute; left: 0; top: 0;
    width: 360px; height: 412px;
    background: linear-gradient(135deg, var(--tone-light) 0%, rgba(68,66,67,0) 75%);
  }
  .back-name {
    position: absolute; right: 28px; top: 128px;
    font-family: "Bebas Neue", sans-serif;
    font-size: 46px; letter-spacing: 2px;
    color: var(--white); line-height: 1;
  }
  .back-title {
    position: absolute; right: 28px; top: 180px;
    font-family: "Montserrat", sans-serif;
    font-size: 15px; letter-spacing: 3px;
    color: var(--gold);
  }
  .gold-rule {
    position: absolute; left: 292px; top: 209px;
    width: 314px; height: 2px;
    background: linear-gradient(90deg, var(--gold), #d3bd75 50%, var(--gold-dark));
  }
  .contact {
    position: absolute; right: 73px;
    text-align: right;
    font-family: "Montserrat", sans-serif;
    font-size: 10.5px; letter-spacing: 2.4px; line-height: 15.5px;
    color: var(--white);
  }
  .contact-phone { top: 256px; }
  .contact-web { top: 292px; }
  .contact-address { top: 340px; }
  .contact-icon { position: absolute; }
  .icon-phone { left: 573px; top: 251px; }
  .icon-mail { left: 570px; top: 305px; }
  .icon-pin { left: 575px; top: 347px; }
</style>
</head>
<body>
<div class="canvas">

  <section class="card-front">
    <div class="front-person">
      <div class="front-name">Laszlo <span class="paren">(</span>Les<span class="paren">)</span> Varga</div>
      <div class="front-title">Owner</div>
    </div>
    <div class="front-mark"></div>
    <div class="front-company">Granite, Zinc and Clay<br>Roofing LLC</div>
  </section>

  <section class="card-back">
    <div class="back-texture" role="img" aria-label="Decorative background area in soft grey tones"></div>

    <div class="back-name">Laszlo (Les) Varga</div>
    <div class="back-title">Owner</div>
    <div class="gold-rule"></div>

    <div class="contact contact-phone">(555) 014-2273</div>
    <div class="contact contact-web">gzcroofingllc@example.com<br>granitezincandclayroofing.example</div>
    <div class="contact contact-address">2870 Millbrook Rd.<br>Millbrook, OH 44000</div>

    <svg class="contact-icon icon-phone" width="26" height="26" viewBox="0 0 26 26" fill="none" stroke="var(--gold)" stroke-width="1.4" stroke-linecap="round" stroke-linejoin="round">
      <path d="M4 3l4 -1 3 6 -2.5 2 q2 5 7 7 l2 -2.5 6 3 -1 4 q-1 2 -4 1.5 q-9 -2 -14.5 -13.5 q-1 -4 0 -6.5z"/>
      <path d="M15 6 a5 5 0 0 1 5 5"/>
      <path d="M15 2 a9 9 0 0 1 9 9"/>
    </svg>
    <svg class="contact-icon icon-mail" width="28" height="22" viewBox="0 0 28 22" fill="none" stroke="var(--gold)" stroke-width="1.4" stroke-linejoin="round">
      <rect x="1" y="1" width="26" height="20"/>
      <path d="M1 1 l13 11 13 -11"/>
      <path d="M1 21 l10 -10 M27 21 l-10 -10"/>
    </svg>
    <svg class="contact-icon icon-pin" width="22" height="30" viewBox="0 0 22 30" fill="none" stroke="var(--gold-dark)" stroke-width="1.4">
      <path d="M11 29 q-10 -12 -10 -18 a10 10 0 0 1 20 0 q0 6 -10 18z"/>
      <circle cx="11" cy="11" r="4"/>
    </svg>
  </section>

</div>
</body>
</html>
```